Folder Design: Mobile Laboratory Service

Need a folder designed for a Mobile Laboratory Service. Folder needs to be very professional and will be used to hold brochure, contract and business card of business. Logos of the company are attached.

Industry/Entity Type

Healthcare

```html
<!DOCTYPE html>
<html lang="en">
<head>
<meta charset="utf-8">
<title>Corvena Mobile Lab – Presentation Folder</title>
<link rel="stylesheet" href="https://fonts.googleapis.com/css2?family=Cinzel:wght@500&family=Montserrat:wght@400;500&display=swap">
<style>
  :root {
    --navy: #061535;
    --navy-deep: #030d26;
    --blue: #1f84e8;
    --blue-light: #5ab3ee;
    --paper: #ffffff;
    --paper-shade: #eef1f4;
    --stage: #e6e8ec;
    --line: #1d4f9a;
  }
  * { box-sizing: border-box; margin: 0; padding: 0; }
  html, body { width: 1200px; height: 1200px; overflow: hidden; }
  body {
    background: var(--stage);
    position: relative;
    font-family: "Montserrat", Arial, sans-serif;
  }
  .spread {
    position: absolute;
    left: 210px;
    width: 780px;
    height: 520px;
    display: flex;
    box-shadow: 0 10px 30px rgba(0,0,0,.18);
  }
  .spread--outside { top: 40px; }
  .spread--inside { top: 640px; }
  .panel { position: relative; width: 390px; height: 520px; overflow: hidden; }
  .panel svg.panel-art { position: absolute; inset: 0; width: 100%; height: 100%; }

  /* back cover */
  .back-cover {
    background: linear-gradient(160deg, var(--navy) 0%, var(--navy-deep) 100%);
    border-right: 1px solid #0d2350;
  }
  .brand {
    position: absolute;
    display: flex;
    align-items: center;
    gap: 10px;
    font-family: "Cinzel", Georgia, serif;
    font-weight: 500;
    color: var(--blue);
    line-height: 1.15;
    letter-spacing: .12em;
  }
  .brand__dot {
    flex: none;
    border: 3px solid var(--blue);
    border-radius: 50%;
  }
  .back-cover .brand { left: 95px; top: 250px; font-size: 19px; }
  .back-cover .brand__dot { width: 34px; height: 34px; }
  .back-cover .rule {
    position: absolute; left: 40px; right: 40px; top: 430px;
    height: 1px; background: var(--line);
  }
  .contact {
    position: absolute; top: 446px;
    display: flex; flex-direction: column; gap: 6px;
    color: #dbe6f6; font-size: 11px; line-height: 1.25;
  }
  .contact--left { left: 42px; }
  .contact--right { left: 212px; }
  .contact__row { display: flex; align-items: flex-start; gap: 6px; }
  .contact__row svg { width: 11px; height: 11px; flex: none; margin-top: 1px; fill: var(--blue-light); }

  /* front cover */
  .front-cover { background: var(--navy); }
  .front-cover .brand { left: 110px; top: 205px; font-size: 26px; }
  .front-cover .brand__dot { width: 44px; height: 44px; }

  /* inside */
  .inside-left { background: linear-gradient(135deg, var(--paper) 0%, var(--paper-shade) 100%); border-right: 1px solid #d6dae0; }
  .inside-right { background: var(--paper); }
</style>
</head>
<body>

<section class="spread spread--outside">
  <div class="panel back-cover">
    <div class="brand">
      <span class="brand__dot"></span>
      <span>Corvena<br>Mobile Lab</span>
    </div>
    <div class="rule"></div>
    <div class="contact contact--left">
      <div class="contact__row">
        <svg viewBox="0 0 24 24"><path d="M6.6 10.8a15 15 0 0 0 6.6 6.6l2.2-2.2c.3-.3.7-.4 1-.2 1.1.4 2.3.6 3.6.6.6 0 1 .4 1 1V20c0 .6-.4 1-1 1A17 17 0 0 1 3 4c0-.6.4-1 1-1h3.5c.6 0 1 .4 1 1 0 1.3.2 2.5.6 3.6.1.3 0 .7-.2 1z"/></svg>
        <span>(000) 000 0000</span>
      </div>
      <div class="contact__row">
        <svg viewBox="0 0 24 24"><path d="M2 5h20v14H2z" fill="none" stroke="#5ab3ee" stroke-width="2"/><path d="M2 5l10 8 10-8" fill="none" stroke="#5ab3ee" stroke-width="2"/></svg>
        <span>email@company.com</span>
      </div>
    </div>
    <div class="contact contact--right">
      <div class="contact__row">
        <svg viewBox="0 0 24 24"><circle cx="12" cy="12" r="9" fill="none" stroke="#5ab3ee" stroke-width="2"/><path d="M3 12h18M12 3c3 3 3 15 0 18M12 3c-3 3-3 15 0 18" fill="none" stroke="#5ab3ee" stroke-width="1.6"/></svg>
        <span>www.company.com</span>
      </div>
      <div class="contact__row">
        <svg viewBox="0 0 24 24"><path d="M12 2a7 7 0 0 0-7 7c0 5 7 13 7 13s7-8 7-13a7 7 0 0 0-7-7zm0 9.5A2.5 2.5 0 1 1 12 6.5a2.5 2.5 0 0 1 0 5z"/></svg>
        <span>123 Name Street, 000<br>Your City, 00000-000</span>
      </div>
    </div>
  </div>

  <div class="panel front-cover">
    <svg class="panel-art" viewBox="0 0 390 520" aria-hidden="true">
      <defs>
        <linearGradient id="swoosh" x1="0" y1="0" x2="1" y2="1">
          <stop offset="0" stop-color="#5ab3ee"/>
          <stop offset="1" stop-color="#1f6fe0"/>
        </linearGradient>
      </defs>
      <rect width="390" height="520" fill="#061535"/>
      <ellipse cx="178" cy="212" rx="318" ry="288" fill="url(#swoosh)"/>
      <ellipse cx="172" cy="205" rx="312" ry="280" fill="#061535"/>
      <ellipse cx="168" cy="198" rx="306" ry="272" fill="#ffffff"/>
    </svg>
    <div class="brand">
      <span class="brand__dot"></span>
      <span>Corvena<br>Mobile Lab</span>
    </div>
  </div>
</section>

<section class="spread spread--inside">
  <div class="panel inside-left"></div>
  <div class="panel inside-right">
    <svg class="panel-art" viewBox="0 0 390 520" aria-hidden="true">
      <defs>
        <linearGradient id="pocket" x1="0" y1="0" x2="1" y2="0.6">
          <stop offset="0" stop-color="#3c93e4"/>
          <stop offset="0.55" stop-color="#5ab3ee"/>
          <stop offset="1" stop-color="#1f7ee6"/>
        </linearGradient>
      </defs>
      <path d="M30 520 L150 330 Q158 318 172 318 H390 V520 Z" fill="url(#pocket)"/>
      <line x1="198" y1="438" x2="222" y2="470" stroke="#2a5a8a" stroke-width="1.2"/>
      <line x1="310" y1="360" x2="334" y2="392" stroke="#2a5a8a" stroke-width="1.2"/>
    </svg>
  </div>
</section>

</body>
</html>
```